Buch-/E-Book-Cover für SEO Experte
Zielgruppe
SEO Experte Rupert L. Wendholm ist Geschäftsführer einer SEO Agentur in Köln und bringt nun 'Das dicke Netz- & Webreklame-Handbuch' auf den Markt. ein kompaktes Werk welches alle Begrifflichkeiten und Konzepte aus der Welt der SEO Optimierung und des Online Marketings einfach erläutert zum nachschlagen in typischer Lexikon Manier.
Titel: Das dicke Netz- & Webreklame-Handbuch
Subtitel: Alle Fragen & Begriffe aus 6 Jahren SEO Agenturarbeit einfach erklärt und kompakt zusammengefasst zum nachschlagen
Aufgabenstellung
Es soll anders sein als das dazugehörige komplementär Buch 'SeitenBau Praxis 2021' aber dennoch im selben Stil gearbeitet sein. Es soll wie ein sehr wertiges großes altes Lexikon wirken mit vielen Seiten. Bitte auch ein stehendes 3D Cover zum normalen Druck Cover liefern.

```html
<!DOCTYPE html>
<html lang="de">
<head>
<meta charset="utf-8">
<title>Das dicke Netz- &amp; Webreklame-Handbuch – Umschlag</title>
<link href="https://fonts.googleapis.com/css2?family=Open+Sans:wght@400;600;700;800&family=Questrial&family=Roboto+Condensed:wght@400&display=swap" rel="stylesheet">
<style>
:root{
  --bg-dark:#23262a;
  --band-light:#f1f1f1;
  --accent:#2f7bc4;
  --text-light:#ffffff;
  --text-dark:#2b2b2b;
  --text-muted:#555;
}
*{margin:0;padding:0;box-sizing:border-box}
html,body{width:1200px;height:560px;overflow:hidden;background:var(--bg-dark)}
.cover{position:relative;width:1200px;height:560px;overflow:hidden;background:var(--bg-dark);font-family:"Open Sans",sans-serif;color:var(--text-light)}
.footer-band{position:absolute;left:0;top:479px;width:1200px;height:81px;background:linear-gradient(180deg,#f5f5f5,#e9e9e9)}
.footer-divider{position:absolute;left:621px;top:479px;width:1px;height:81px;background:#d4d4d4}

/* back cover */
.back-headline{position:absolute;left:257px;top:46px;font-size:21px;line-height:25px;font-weight:400}
.back-headline strong{display:block;font-size:25px;line-height:30px;font-weight:800}
.back-copy{position:absolute;left:257px;top:119px;font-size:10.1px;line-height:13.3px;letter-spacing:-.1px}
.back-copy p{margin-bottom:8px}
.back-copy span{display:block;white-space:nowrap}
.learn-label{position:absolute;left:258px;top:245px;font-size:11px;font-weight:700}
.contents-box{position:absolute;left:258px;top:261px;width:253px;height:97px;background:#fff;color:#3a3a3a;display:flex;flex-direction:column;align-items:center;justify-content:center;text-align:center;font-weight:700;font-size:22px;line-height:25px}
.author-box{position:absolute;left:257px;top:369px;width:280px;height:79px;background:linear-gradient(90deg,#f7f7f7,#e6e6e6);border-top:1px solid #9fc4e2;box-shadow:0 3px 8px rgba(0,0,0,.4);display:flex}
.author-photo{flex:0 0 69px;width:69px;height:100%;background:linear-gradient(135deg,#c9c9c9,#7a7a7a 55%,#2a2f3a)}
.author-bio{padding:10px 4px 0 10px;font-size:8.3px;line-height:10.2px;color:var(--text-dark);letter-spacing:-.05px}
.author-bio span{display:block;white-space:nowrap}
.author-bio b{font-weight:700}

/* spine */
.spine-title{position:absolute;left:611px;top:41px;writing-mode:vertical-rl;font-weight:800;font-size:15px;letter-spacing:.2px;white-space:nowrap}
.spine-sub{position:absolute;left:594px;top:326px;width:14px;height:134px;border:1px solid #fff;writing-mode:vertical-rl;font-size:7.4px;display:flex;align-items:center;justify-content:center;white-space:nowrap}
.spine-sub b{font-weight:700;margin-bottom:2px}
.spine-author{position:absolute;left:592px;top:484px;writing-mode:vertical-rl;font-size:7.6px;line-height:9px;color:var(--text-muted);text-align:left}

/* front cover */
.badge-new{position:absolute;left:636px;top:0;width:78px;height:25px}
.front-title{position:absolute;left:622px;width:378px;top:34px;text-align:center;font-weight:600;font-size:28px;line-height:38.5px;letter-spacing:-.3px}
.front-title .accent{color:var(--accent);font-weight:700}
.front-subtitle{position:absolute;left:622px;width:378px;top:160px;text-align:center;font-family:"Questrial",sans-serif;font-size:13.6px}
.front-art{position:absolute;left:650px;top:225px;width:310px;height:183px}
.front-claim{position:absolute;left:622px;width:378px;top:438px;text-align:center;font-family:"Roboto Condensed",sans-serif;font-size:22px;letter-spacing:-.4px}
.front-author{position:absolute;left:622px;width:378px;top:515px;text-align:center;font-size:9.6px;color:var(--text-dark);letter-spacing:.1px}

/* partner row */
.partners-label{position:absolute;left:230px;width:330px;top:488px;text-align:center;font-size:8.4px;font-weight:700;color:#444}
.partners{position:absolute;left:228px;width:336px;top:514px;display:flex;justify-content:space-between;align-items:center;font-size:7px;font-weight:700;color:#4a4a4a}
.partner{display:flex;align-items:center;gap:3px;white-space:nowrap}
.partner i{display:block;width:9px;height:9px;border-radius:50%;background:#6a6a6a}
</style>
</head>
<body>
<div class="cover">
  <div class="footer-band"></div>
  <div class="footer-divider"></div>

  <!-- back cover -->
  <h2 class="back-headline">Nehmen Sie ihren SEO-Erfolg<strong>jetzt selbst in die Hand!</strong></h2>
  <div class="back-copy">
    <p>
      <span>Der <b>Erfahrungsschatz</b> aus über 6 Jahren hauptberuflicher</span>
      <span>SEO-Optimierung für Seitenwerk kompakt und gut aufbereitet</span>
      <span>zusammengefasst. Sie erhalten das komplette Rüstzeug, mit</span>
      <span>dem mein Team und ich in den letzten Jahren <b>überragende</b></span>
      <span><b>SEO-Erfolge</b> für unsere Kunden erzielt haben.</span>
    </p>
    <p>
      <span>Alle <b>Fragen &amp; Begriffe</b> aus <b>6 Jahren</b> SEO Agenturarbeit werden</span>
      <span>Ihnen hier einfach erklärt und kompakt zusammengefasst und</span>
      <span>das alles zum praktischen nachschlagen.</span>
    </p>
  </div>
  <div class="learn-label">Sie werden u.a lernen:</div>
  <div class="contents-box"><span>PLATZHALTER</span><span>(Inhalt des Lexikons)</span></div>
  <div class="author-box">
    <div class="author-photo" role="img" aria-label="Porträtfoto des Autors"></div>
    <p class="author-bio">
      <span><b>Rupert Wendholm</b> ist Geschäftsführer einer</span>
      <span>Kölner SEO-Agentur und arbeitete bereits als</span>
      <span><b>Findmal-Trainer</b>, IHK &amp; HWK Referent, Digital</span>
      <span>Marketing Berater und als Dozent für</span>
      <span>Suchmaschinenoptimierung am Institut</span>
      <span>für Medien in Köln.</span>
    </p>
  </div>

  <div class="partners-label">Bekannt aus / Veröffentlicht bei:</div>
  <div class="partners">
    <span class="partner"><i></i>Rankmesser</span>
    <span class="partner">Gewerkhaus Rhein</span>
    <span class="partner">Kammer West</span>
    <span class="partner">Wachstumsnetz</span>
    <span class="partner">Lernforum Medien</span>
    <span class="partner">Suchtage</span>
  </div>

  <!-- spine -->
  <div class="spine-title">NETZ- &amp; WEBREKLAME-HANDBUCH</div>
  <div class="spine-sub"><span><b>6 Jahre</b> SEO Agenturarbeit erklärt</span></div>
  <div class="spine-author">RUPERT<br>WENDHOLM</div>

  <!-- front cover -->
  <svg class="badge-new" viewBox="0 0 78 25" aria-label="Neu">
    <polygon points="6,0 78,0 72,25 0,25" fill="#fff"/>
    <text x="39" y="19" text-anchor="middle" font-family="Open Sans, sans-serif" font-weight="800" font-size="17" fill="#2f7bc4">NEU!</text>
  </svg>
  <h1 class="front-title">DAS <span class="accent">DICKE</span><br>NETZ- &amp; WEBREKLAME-<br>HANDBUCH</h1>
  <p class="front-subtitle">6 Jahre SEO Agenturarbeit zum Nachschlagen</p>
  <svg class="front-art" viewBox="0 0 310 183" role="img" aria-label="Illustration eines Abreißkalenders mit der Zahl 6 und davonfliegenden Kalenderblättern">
    <defs>
      <linearGradient id="artFill" x1="0" y1="0" x2="1" y2="1">
        <stop offset="0" stop-color="#2f7bc4" stop-opacity=".55"/>
        <stop offset=".5" stop-color="#e8eef5" stop-opacity=".35"/>
        <stop offset="1" stop-color="#23262a" stop-opacity="0"/>
      </linearGradient>
    </defs>
    <rect width="310" height="183" rx="10" fill="url(#artFill)"/>
  </svg>
  <p class="front-claim">IHR WEG AN DIE SPITZE!</p>
  <p class="front-author">RUPERT L. WENDHOLM</p>
</div>
</body>
</html>
```